Distribution/Printing company needs a web site to inform prospective customers on what we do.

Distribution/Printing/Packaging company needs a web site to inform prospective customers on what we do. Please look at our direct to consumer web site (under development) for an idea of the product lines we sell: storedev.thebrindlestock.com
Logo files are attached as is a flyer that is under development which contains other information about the company (this is to be used for content- not to be posted as is). The web site should be focused on our business customer base and is not intended to be direct to consumer. Site should have a link to our consumer web site.
Site design should be mobile friendly, or mobile could be redirected to a mobile version. This web site will be strictly informational and will not be designed for any sales transactions.

Target Market(s)

Manufacturing and retail businesses, any other multi-site business that would benefit from centralized pricing and budget controls we can provide (banks, medical/dental offices, educational facilities, etc).

Requirements
Must have
• 1) Top level menu: Products, about us, locations, contact us, news
• 2) page with news/promotions that is easily updated
• 3) "contact us" form (name, company, phone, email address) email link
• 4) link to www.store.thebrindlestock.com with information that lower pricing is available for businesses
• 5) SEO keywords
• 6) Link to powerpoint presentation file
Nice to have
• 1) our phone number should appear on every page near the top

```html
<!DOCTYPE html>
<html lang="en">
<head>
<meta charset="utf-8">
<title>Tall Pines Supply — Packaging, Printing, Distribution</title>
<meta name="keywords" content="distribution, packaging, flexographic printing, supply chain, procurement, warehousing, inventory management">
<link rel="stylesheet" href="https://fonts.googleapis.com/css2?family=Arimo:wght@400;700&family=Josefin+Sans:wght@300;400&display=swap">
<style>
:root{
  --ink:#1c1c1c;
  --text:#333333;
  --muted:#9a9a9a;
  --rule:#cfcfcf;
  --white:#ffffff;
  --charcoal:#262626;
  --band-dark:#2a2a2a;
  --slate-1:#4a5660;
  --slate-2:#1d2328;
  --footer:#cdc4bd;
  --footer-rule:#b3aaa3;
  --social:#2f3f8a;
}
*{margin:0;padding:0;box-sizing:border-box}
html,body{width:1200px;height:3019px;overflow:hidden}
body{position:relative;background:var(--white);font-family:"Arimo",Arial,sans-serif;color:var(--text)}
a{color:inherit;text-decoration:none}
.section{position:absolute;left:0;width:1200px}
.abs{position:absolute}
.heading-line{position:absolute;left:155px;width:890px;display:flex;align-items:center;gap:28px;font-family:"Josefin Sans",sans-serif;font-weight:300;font-size:30px;white-space:nowrap}
.heading-line::before,.heading-line::after{content:"";flex:1;height:1px;background:currentColor;opacity:.45}
.btn{position:absolute;display:flex;align-items:center;justify-content:center;font-family:"Josefin Sans",sans-serif;font-size:17px;letter-spacing:.5px;white-space:nowrap}

/* header */
.site-header{top:0;height:134px;background:var(--white)}
.brand{left:155px;top:22px;color:var(--ink)}
.brand-name{font-family:"Arimo",sans-serif;font-weight:700;font-size:17px;letter-spacing:.3px;display:block;margin-top:44px}
.brand-tagline{font-size:12px;display:block;margin-top:3px}
.phone{left:837px;top:22px;display:flex;align-items:center;gap:14px;font-size:28px;color:var(--ink)}
.phone-icon{width:43px;height:43px;border-radius:50%;background:var(--ink);display:flex;align-items:center;justify-content:center}
.main-nav{top:95px;left:0;width:1200px;height:20px}
.main-nav a{position:absolute;font-size:15px;color:var(--ink)}

/* hero */
.hero{top:134px;height:358px;background:linear-gradient(180deg,#a89a82 0%,#c9a35a 30%,#8c6f55 60%,#b58d5d 100%)}
.hero-photo{position:absolute;inset:0;background:radial-gradient(ellipse at 50% 45%,rgba(230,225,215,.75) 0%,rgba(200,160,110,.3) 40%,rgba(90,70,60,.25) 100%)}
.hero-title{top:160px;left:0;width:1200px;text-align:center;color:var(--white);font-weight:700;font-size:34px;text-shadow:0 1px 3px rgba(0,0,0,.35)}
.hero .btn{left:544px;top:233px;width:114px;height:43px;background:rgba(40,40,40,.8);border:2px solid rgba(255,255,255,.6);color:var(--white)}
.dots{position:absolute;display:flex;gap:5px}
.dots span{width:10px;height:10px;border-radius:50%;border:1px solid var(--white);background:transparent}
.dots span.on{background:var(--white)}

/* services */
.services{top:492px;height:414px;border-bottom:1px solid #e3e3e3}
.services .heading-line{top:54px;color:var(--text)}
.service{position:absolute;width:260px;text-align:center}
.service-icon{width:119px;height:119px;border-radius:50%;background:var(--ink);border:5px solid #e9e9e9;margin:0 auto;display:flex;align-items:center;justify-content:center}
.service h3{font-size:13px;font-weight:400;color:var(--ink);margin-top:42px}
.service p{font-size:12.5px;color:var(--muted);line-height:17px;margin:12px auto 0;width:230px}
.slide-arrow{position:absolute}

/* web platform */
.web-platform{top:906px;height:529px;background:linear-gradient(180deg,var(--slate-1) 0%,#343d45 45%,var(--slate-2) 100%);color:var(--white)}
.web-platform .heading-line{top:52px;color:var(--white)}
.keyboard-visual{position:absolute;left:0;top:240px;width:1200px;height:289px;background:linear-gradient(180deg,rgba(120,130,140,0) 0%,rgba(150,158,165,.35) 50%,rgba(60,66,72,.2) 100%)}
.devices-visual{position:absolute;left:155px;top:147px;width:324px;height:195px;background:linear-gradient(180deg,rgba(255,255,255,.22),rgba(255,255,255,.12));border-radius:10px}
.feature-list{position:absolute;left:583px;top:146px;list-style:none;width:480px}
.feature-list li{display:flex;gap:16px;font-size:17px;line-height:21px;margin-bottom:17px}
.feature-list li svg{flex:none;margin-top:1px}

/* highlight cards */
.highlights{top:1435px;height:360px}
.card{position:absolute;top:60px;width:201px}
.card-image{height:139px;border:1px solid #ddd;padding:4px;background:var(--white)}
.card-image div{width:100%;height:100%}
.card p{font-size:13px;line-height:16px;color:var(--muted);margin-top:14px}

/* printing */
.printing{top:1795px;height:454px;background:var(--band-dark);color:var(--white)}
.printing .heading-line{top:46px;color:var(--white)}
.product-visual{left:162px;top:158px;width:403px;height:216px;border-radius:6px;background:linear-gradient(90deg,#3f8c3a 0%,#e8e2cf 30%,#3c6bb0 55%,#d9c23e 75%,#4f9a44 100%)}
.print-specs{position:absolute;left:660px;top:158px;list-style:none;font-weight:700;font-size:17px}
.print-specs li{margin-bottom:19px;line-height:20px}
.printing .btn{left:660px;top:303px;width:236px;height:43px;border:2px solid #999;color:var(--white);font-size:15px}

/* partners */
.partners{top:2249px;height:394px}
.map-visual{position:absolute;left:130px;top:0;width:940px;height:394px;background:radial-gradient(ellipse at 50% 40%,rgba(220,220,220,.55) 0%,rgba(240,240,240,.3) 55%,rgba(255,255,255,0) 80%)}
.partners .heading-line{top:104px;color:var(--text)}
.partners .lede{position:absolute;top:168px;width:1200px;text-align:center;font-size:15px;color:#888}
.partners .btn{left:470px;top:222px;width:264px;height:50px;background:var(--charcoal);color:var(--white);border:2px solid #bbb}

/* footer */
.site-footer{top:2643px;height:376px;background:var(--footer);border-top:4px solid #b9b0a9}
.footer-col h4{font-size:17px;font-weight:700;color:var(--ink);letter-spacing:.3px}
.history p{font-size:13px;line-height:17px;color:#333;margin-top:24px;width:290px}
.quick-links ul{margin-top:22px;padding-left:16px;font-size:13px;line-height:21.6px;color:#333}
.contact-list{list-style:none;margin-top:22px;font-size:13px;line-height:17px;color:#333}
.contact-list li{display:flex;gap:10px;margin-bottom:14px}
.newsletter p{font-size:13px;color:#333;margin-top:22px}
.email-field{margin-top:14px;width:188px;height:32px;border:1px solid #555;background:var(--white);display:flex;align-items:center;justify-content:space-between;padding-left:8px;font-size:13px;color:#333}
.email-field span.go{width:34px;height:30px;background:var(--ink);display:flex;align-items:center;justify-content:center}
.social{position:absolute;left:857px;top:223px;display:flex;gap:6px}
.social span{width:42px;height:42px;border-radius:50%;background:var(--social);border:2px solid #e0d8d2}
.footer-rule{position:absolute;left:155px;top:288px;width:890px;height:1px;background:var(--footer-rule)}
.copyright{position:absolute;top:323px;width:1200px;text-align:center;font-size:13px;color:#333}
</style>
</head>
<body>

<header class="section site-header">
  <a class="abs brand" href="#">
    <span class="brand-name">TALL PINES SUPPLY</span>
    <span class="brand-tagline">Packaging • Printing • Distribution</span>
  </a>
  <div class="abs phone">
    <span class="phone-icon"><svg width="20" height="20" viewBox="0 0 24 24"><path fill="#fff" d="M6.6 10.8c1.4 2.8 3.8 5.1 6.6 6.6l2.2-2.2c.3-.3.7-.4 1-.2 1.1.4 2.3.6 3.6.6.6 0 1 .4 1 1V20c0 .6-.4 1-1 1C10.6 21 3 13.4 3 4c0-.6.4-1 1-1h3.5c.6 0 1 .4 1 1 0 1.3.2 2.5.6 3.6.1.3 0 .7-.2 1z"/></svg></span>
    (555) 014-2290
  </div>
  <nav class="section main-nav">
    <a href="#" style="left:507px">Home</a>
    <a href="#" style="left:591px">Products</a>
    <a href="#" style="left:690px">About us</a>
    <a href="#" style="left:792px">Locations</a>
    <a href="#" style="left:898px">Contact us</a>
    <a href="#" style="left:1010px">News</a>
  </nav>
</header>

<section class="section hero">
  <div class="hero-photo" role="img" aria-label="Photo of a supermarket aisle lined with stocked shelves"></div>
  <h1 class="abs hero-title">Better Supply chain performance at Lower Cost</h1>
  <a class="btn" href="#">READ MORE</a>
  <div class="dots" style="left:569px;top:325px"><span class="on"></span><span></span><span></span><span></span><span></span></div>
</section>

<section class="section services">
  <h2 class="heading-line">How can Tall Pines Improve Your Business?</h2>
  <svg class="slide-arrow" style="left:132px;top:213px" width="22" height="44" viewBox="0 0 22 44"><path d="M20 2 2 22l18 20" fill="none" stroke="#cfcfcf" stroke-width="2"/></svg>
  <svg class="slide-arrow" style="left:1046px;top:213px" width="22" height="44" viewBox="0 0 22 44"><path d="M2 2l18 20L2 42" fill="none" stroke="#cfcfcf" stroke-width="2"/></svg>

  <div class="service" style="left:144px;top:118px">
    <div class="service-icon"><svg width="56" height="40" viewBox="0 0 56 40"><path d="M4 12l10-6 10 4 8-4 10 4 10-2v16l-10 6-12 8-10-6-16-8z" fill="#fff"/><path d="M20 22l8 6M24 18l8 6" stroke="#1c1c1c" stroke-width="2"/></svg></div>
    <h3>Sourcing and Procurement Support</h3>
    <p>Let us manage your suppliers while you manage your business, saving money and time</p>
  </div>
  <div class="service" style="left:472px;top:118px">
    <div class="service-icon"><svg width="48" height="44" viewBox="0 0 48 44"><path d="M4 4h6l4 26h26" fill="none" stroke="#fff" stroke-width="3"/><rect x="16" y="10" width="12" height="14" fill="#fff"/><rect x="30" y="14" width="10" height="10" fill="#fff"/><circle cx="18" cy="37" r="4" fill="#fff"/><circle cx="36" cy="37" r="4" fill="#fff"/></svg></div>
    <h3>Warehousing and Fulfillment</h3>
    <p>Our distribution centers allow us to efficiently manage fulfillment and delivery of supplies</p>
  </div>
  <div class="service" style="left:815px;top:118px">
    <div class="service-icon"><svg width="40" height="48" viewBox="0 0 40 48"><rect x="3" y="5" width="34" height="41" rx="2" fill="none" stroke="#fff" stroke-width="3"/><rect x="13" y="1" width="14" height="8" fill="#fff"/><path d="M9 20l3 3 5-5M9 33l3 3 5-5" fill="none" stroke="#fff" stroke-width="2.5"/><path d="M21 21h10M21 34h10" stroke="#fff" stroke-width="3"/></svg></div>
    <h3>Inventory Management</h3>
    <p>We allow our customers to remain competitive while avoiding overstocks and shortages</p>
  </div>
</section>

<section class="section web-platform">
  <div class="keyboard-visual" role="img" aria-label="Photo of a computer keyboard on a desk"></div>
  <h2 class="heading-line">WEB PLATFORM DESIGN</h2>
  <div class="devices-visual" role="img" aria-label="Illustration of a phone, desktop monitor and tablet"></div>
  <ul class="feature-list">
    <li><svg width="20" height="18" viewBox="0 0 20 18"><rect x="1" y="1" width="18" height="12" fill="none" stroke="#fff" stroke-width="2"/><path d="M6 17h8M10 13v4" stroke="#fff" stroke-width="2"/></svg>User-friendly storefront Web interface</li>
    <li><svg width="20" height="18" viewBox="0 0 20 18"><circle cx="10" cy="5" r="4" fill="#fff"/><path d="M2 18c0-5 4-7 8-7s8 2 8 7z" fill="#fff"/></svg>Each user has their own User ID and password</li>
    <li><svg width="20" height="18" viewBox="0 0 20 18"><path d="M1 2h3l2 10h11l2-7H6" fill="none" stroke="#fff" stroke-width="2"/><circle cx="8" cy="16" r="1.6" fill="#fff"/><circle cx="16" cy="16" r="1.6" fill="#fff"/></svg>Purchases are mapped to the particular User/ Department</li>
    <li><svg width="20" height="20" viewBox="0 0 20 20"><rect x="2" y="1" width="14" height="18" fill="none" stroke="#fff" stroke-width="2"/><path d="M5 6h8M5 10h8M5 14h5" stroke="#fff" stroke-width="2"/></svg>Dashboard allows User to quickly review most current<br>order and previous orders.</li>
    <li><svg width="20" height="16" viewBox="0 0 20 16"><rect x="1" y="2" width="18" height="12" fill="#fff"/><path d="M1 2l9 7 9-7" fill="none" stroke="#3a434b" stroke-width="1.5"/></svg>Communicate messages to users via the website.</li>
    <li><svg width="20" height="18" viewBox="0 0 20 18"><path d="M10 1C5 1 1 4 1 8c0 2 1 4 3 5l-1 4 5-3h2c5 0 9-3 9-7s-4-6-9-6z" fill="#fff"/></svg>Chat with TPS Customer Support regarding your orders</li>
  </ul>
  <div class="dots" style="left:588px;top:450px"><span class="on"></span><span></span></div>
</section>

<section class="section highlights">
  <article class="card" style="left:155px">
    <div class="card-image"><div role="img" aria-label="Screenshot of the online ordering dashboard" style="background:linear-gradient(180deg,#dfe9f5,#f7f9fc 30%,#e9eef5)"></div></div>
    <p>We pride ourselves on the level of integration TPS achieves with each of our customers.</p>
  </article>
  <article class="card" style="left:384px">
    <div class="card-image"><div role="img" aria-label="Photo of a courier delivering boxes at a front door" style="background:linear-gradient(135deg,#5a3a22,#b9865a 55%,#e8d5b8)"></div></div>
    <p style="text-align:justify">Our Promise 100% ON-TIME DELIVERY OF SUPPLIES 100% WHOLE ORDER FILL RATE ASSURANCE 24 HOUR REPLACEMENT GUARANTEE</p>
  </article>
  <article class="card" style="left:615px">
    <div class="card-image"><div role="img" aria-label="Photo of a custom printed corrugated shipping carton" style="background:linear-gradient(160deg,#f3f1ea,#c9a573 55%,#a88457)"></div></div>
    <p>We offer full service custom packaging: Design, Source and Deliver: Standard Packaging, Branded and Private Label</p>
  </article>
  <article class="card" style="left:846px">
    <div class="card-image"><div role="img" aria-label="Photo of a store floor with a grand opening floor graphic" style="background:linear-gradient(180deg,#eef0ee,#c7d9c4 55%,#9fc2a6)"></div></div>
    <p>For Store Opening and remodel, we offer assembly and shipping of store fixtures, packaging materials, corrugated cartons &amp; displays, bulbs &amp; electrical and much more</p>
  </article>
</section>

<section class="section printing">
  <h2 class="heading-line">FULL SERVICE FLEXOGRAPHIC PRINTING</h2>
  <div class="abs product-visual" role="img" aria-label="Photo of printed flexible packaging bags and pouches"></div>
  <ul class="print-specs">
    <li>Up to 8 colors</li>
    <li>Paper, Synthetic Label, Tags,BOPP, +Others</li>
    <li>Fully Integrated, SQF Certified Flexographic Printing</li>
  </ul>
  <a class="btn" href="#">BOOK YOUR ORDER NOW!</a>
</section>

<section class="section partners">
  <div class="map-visual" role="img" aria-label="Faint world map background"></div>
  <h2 class="heading-line">Partnerships with 2,000 World Class Suppliers</h2>
  <p class="lede">Offering multiple capabilities Adding value for both customers and suppliers</p>
  <a class="btn" href="#">BOOK YOUR ORDER NOW!</a>
</section>

<footer class="section site-footer">
  <div class="abs footer-col history" style="left:160px;top:57px">
    <h4>OUR HISTORY</h4>
    <p>For over 20 years, Tall Pines has offered supply chain solutions through an innovative technology platform that helps companies of all sizes lower costs and improve performance. A break in the supply chain can reduce a company's revenues, inflate costs, or threaten production and distribution so we provide the supply chain flexibility, agility and dependability that our customers need to thrive.</p>
  </div>
  <div class="abs footer-col quick-links" style="left:470px;top:57px">
    <h4>QUICK LINKS</h4>
    <ul>
      <li>Home</li><li>Products</li><li>About us</li><li>Locations</li><li>Contact us</li><li>News</li>
    </ul>
  </div>
  <div class="abs footer-col" style="left:626px;top:57px">
    <h4>CONTACT US</h4>
    <ul class="contact-list">
      <li><svg width="14" height="20" viewBox="0 0 14 20"><path d="M7 0C3 0 0 3 0 7c0 5 7 13 7 13s7-8 7-13c0-4-3-7-7-7zm0 10a3 3 0 110-6 3 3 0 010 6z" fill="#1c1c1c"/></svg><span>4120 Harbor Mill Road,<br>Suite 12 Riverton,<br>FL 32000</span></li>
      <li><svg width="14" height="16" viewBox="0 0 24 24"><path fill="#1c1c1c" d="M6.6 10.8c1.4 2.8 3.8 5.1 6.6 6.6l2.2-2.2c.3-.3.7-.4 1-.2 1.1.4 2.3.6 3.6.6.6 0 1 .4 1 1V20c0 .6-.4 1-1 1C10.6 21 3 13.4 3 4c0-.6.4-1 1-1h3.5c.6 0 1 .4 1 1 0 1.3.2 2.5.6 3.6.1.3 0 .7-.2 1z"/></svg><span>(555) 014 - 2290</span></li>
      <li><svg width="16" height="14" viewBox="0 0 16 14"><rect x="0" y="1" width="16" height="12" fill="#1c1c1c"/><path d="M0 1l8 6 8-6" fill="none" stroke="#cdc4bd" stroke-width="1.3"/></svg><span>info@tallpinessupply.com</span></li>
    </ul>
  </div>
  <div class="abs footer-col newsletter" style="left:857px;top:57px">
    <h4>CONNECT US WITH</h4>
    <p>Signup for Our newsletter</p>
    <div class="email-field">Enter your email<span class="go"><svg width="18" height="16" viewBox="0 0 18 16"><path d="M0 7L18 0 14 16 9 11 15 3 7 10z" fill="#fff"/></svg></span></div>
  </div>
  <div class="social"><span></span><span></span><span></span><span></span></div>
  <div class="footer-rule"></div>
  <p class="copyright">Copyright © 2015 Tall Pines Supply. All right Reserved.</p>
</footer>

</body>
</html>
```